Postcard promoting HIPAA services, including training, risk assessments, policies, etc.

I am planning a campaign to medical practices advertising HIPAA services. The primary message to convey is that HIPAA random audits are beginning in early 2016, is your practice ready. I need a full-color front design, 4.25 x 6. The design should convey some sense of urgency, and should be dramatic enough to catch the attention of a busy medical practice.

Target Market(s)

Medical, dental, chiropractic, and counseling practices

Industry/Entity Type

Doctor

Font styles to use
Sans Serif

Requirements
Must have
• Sense of urgency, specific mention of upcoming HIPAA audits, feeling that smaller practices are not exempt.

```html
<!DOCTYPE html>
<html lang="en">
<head>
<meta charset="utf-8">
<title>HIPAA Audit Postcard</title>
<link href="https://fonts.googleapis.com/css2?family=Oswald:wght@500;600&family=Open+Sans:wght@400;600&family=Quicksand:wght@500&display=swap" rel="stylesheet">
<style>
  :root {
    --page: #e9e9e9;
    --sky: #3fc2f2;
    --sky-deep: #22a9e6;
    --white: #ffffff;
    --ink: #1c2430;
    --red: #c8102e;
    --orange: #e2562a;
    --charcoal: #3a3a3a;
    --wood-light: #e3bf92;
    --wood-dark: #c48f58;
    --screen: #1f2226;
    --paper: #f6f4f0;
    --steel: #5b6168;
  }
  * { box-sizing: border-box; margin: 0; padding: 0; }
  html, body { width: 884px; height: 1200px; overflow: hidden; }
  body { background: var(--page); position: relative; font-family: "Open Sans", sans-serif; }

  .card { position: absolute; left: 42px; width: 800px; height: 566px; overflow: hidden; box-shadow: 0 4px 14px rgba(0,0,0,.25); }

  /* Front */
  .front { top: 20px; background: var(--sky); }
  .front .photo { position: absolute; inset: 0 0 auto 0; height: 400px;
    background: linear-gradient(105deg,
      var(--screen) 0%, #3a3d42 20%, #d8d8d8 30%,
      var(--wood-light) 38%, var(--paper) 50%, var(--paper) 56%,
      var(--wood-light) 66%, #b98552 78%, var(--wood-dark) 100%); }
  .front .wave { position: absolute; left: 0; top: 290px; width: 800px; height: 276px; }
  .front .envelope { position: absolute; left: 12px; top: 372px; width: 168px; height: 180px;
    background: linear-gradient(180deg, #d9303a 0%, #e86a6a 22%, #f3f3f3 45%, #d2d2d2 100%);
    border: 6px solid var(--white); box-shadow: 0 2px 6px rgba(0,0,0,.2); }
  .brand { font-family: "Quicksand", sans-serif; font-weight: 500; color: var(--ink); display: flex; align-items: center; gap: 8px; white-space: nowrap; }
  .brand .mark { width: 14px; height: 14px; background: var(--orange); }
  .front .brand { position: absolute; right: 40px; top: 372px; font-size: 36px; }
  .front .tagline { position: absolute; right: 40px; top: 420px; font-size: 10px; color: rgba(255,255,255,.55); }
  .headline { position: absolute; left: 190px; right: 10px; text-align: center; color: var(--white);
    font-family: "Oswald", sans-serif; font-weight: 600; letter-spacing: .2px; white-space: nowrap; }
  .headline.lead { top: 440px; font-size: 33px; }
  .headline.ask { top: 492px; font-size: 33px; }
  .headline .accent { color: var(--red); }

  /* Back */
  .back { top: 614px; background: var(--white); }
  .back .panel { position: absolute; left: 0; top: 0; width: 460px; height: 500px;
    background: linear-gradient(180deg, var(--sky), var(--sky-deep)); }
  .back .brand { position: absolute; left: 30px; top: 86px; font-size: 22px; }
  .back .brand .mark { width: 11px; height: 11px; }
  .back .tagline { position: absolute; left: 30px; top: 116px; font-size: 8px; color: rgba(255,255,255,.6); }
  .contact { position: absolute; left: 190px; top: 24px; width: 258px; padding: 8px 12px;
    background: var(--charcoal); font-family: "Oswald", sans-serif; font-weight: 500; line-height: 1.2; white-space: nowrap; }
  .contact .phone { color: var(--white); font-size: 21px; }
  .contact .url { color: var(--orange); font-size: 18px; }
  .copy { position: absolute; left: 36px; top: 136px; width: 390px; font-size: 14px; line-height: 1.4; color: var(--ink); }
  .copy p { margin-bottom: 12px; }
  .checklist { list-style: none; width: 190px; margin: -4px 0 12px 14px; }
  .checklist li { position: relative; padding-left: 20px; }
  .checklist li::before { content: "\25C6"; position: absolute; left: 0; font-size: 9px; top: 4px; }
  .callout { position: absolute; left: 268px; top: 238px; font-family: "Oswald", sans-serif; font-weight: 500;
    font-size: 20px; color: var(--ink); white-space: nowrap; }
  .gavel { position: absolute; left: 290px; top: 280px; width: 130px; height: 80px; border-radius: 8px;
    background: linear-gradient(150deg, #d7dbe0 0%, #8e959c 45%, var(--steel) 100%); }
</style>
</head>
<body>

<section class="card front">
  <div class="photo" role="img" aria-label="Photo of a wooden desk with a tablet showing X-ray scans, a pen, and a spiral notepad hand-lettered with HIPAA Compliance Plan"></div>
  <svg class="wave" viewBox="0 0 800 276" preserveAspectRatio="none" aria-hidden="true">
    <path d="M0 60 C 200 110, 420 120, 560 70 C 660 35, 740 10, 800 0 L800 276 L0 276 Z" fill="var(--sky)"/>
  </svg>
  <div class="envelope" role="img" aria-label="Illustration of an opened envelope with a letter reading You're Getting Audited"></div>
  <div class="brand"><span class="mark"></span>Meridia IT</div>
  <div class="tagline">Smart IT for Busy Practices</div>
  <h1 class="headline lead">Random HIPAA audits begin in early 2016.</h1>
  <h2 class="headline ask">Is <span class="accent">your</span> practice ready?</h2>
</section>

<section class="card back">
  <div class="panel">
    <div class="brand"><span class="mark"></span>Meridia IT</div>
    <div class="tagline">Smart IT for Busy Practices</div>
    <div class="contact">
      <div class="phone">LET'S TALK: 555-014-2290</div>
      <div class="url">www.meridiait.com/hipaa</div>
    </div>
    <div class="copy">
      <p>HHS has recently announced random audits, to begin in early 2016.</p>
      <p>If they show up at your door, they will ask for:</p>
      <ul class="checklist">
        <li>Your HIPAA compliance plan</li>
        <li>A security Policy document</li>
        <li>A risk assessment</li>
        <li>Evidence of employee training</li>
        <li>And much more</li>
      </ul>
      <p>If you don't have everything on the list, or you are not sure if your effort is correct and complete, Meridia IT can help, with affordable hourly and fixed-price service to get your practice ready for audit. Contact us today for a free compliance assessment.</p>
    </div>
    <div class="callout">Are You Compliant?</div>
    <div class="gavel" role="img" aria-label="Illustration of a judge's gavel"></div>
  </div>
</section>

</body>
</html>
```